Lenny Marsh Business Cards
DJ Lenny Marsh
Simple
Lenny Marsh
DJ
4731 Corliss Street Los Angeles, CA 90041
djlennymarsh@postvale.com
djlennymarsh.com
I'd like to have a seperate email listing shown as " Bookings - kt@quillsoundagency.com"
-also under website show twitter.com/djlennymarsh
- do not show address on card
Logo on the front all other info on the back
I would like to see the color version titled "lenny-blue-grey" as well as the "lenny-white-grey"
please also try with the color "lenny-black-white". The back of the card should be very simple, nothing too crazy
Please use this logo as well. No need for headphones on the back or any fancy graphics. Please just simple text with the information I provided.Thank you.

```html
<!DOCTYPE html>
<html lang="en">
<head>
<meta charset="utf-8">
<title>Lenny Marsh Business Cards</title>
<link rel="stylesheet" href="https://fonts.googleapis.com/css2?family=Fredoka:wght@400;500;600&display=swap">
<style>
  :root {
    --page: #ffffff;
    --card: #5d5d5f;
    --card-glow: #79797c;
    --yellow: #ece41a;
    --red: #e0241f;
    --emblem: #8a8a8d;
  }
  * { margin: 0; padding: 0; box-sizing: border-box; }
  html, body {
    width: 1200px;
    height: 751px;
    overflow: hidden;
    background: var(--page);
  }
  .sheet {
    position: relative;
    width: 1200px;
    height: 751px;
    font-family: "Fredoka", sans-serif;
  }
  .card {
    position: absolute;
    width: 523px;
    border-radius: 24px;
    overflow: hidden;
    background-color: var(--card);
  }
  .card--top { top: 43px; height: 348px; }
  .card--bottom { top: 406px; height: 333px; }
  .card--left { left: 53px; }
  .card--right { left: 629px; }

  .card--front {
    background-image: radial-gradient(circle at 32% 22%, var(--card-glow) 0, var(--card-glow) 250px, transparent 252px);
  }
  .card--back {
    background-image: radial-gradient(circle at 88% -6%, var(--card-glow) 0, var(--card-glow) 300px, transparent 302px);
  }

  .wordmark {
    position: absolute;
    left: 0;
    right: 0;
    top: 50%;
    transform: translateY(-50%);
    text-align: center;
    font-weight: 600;
    font-size: 52px;
    line-height: 1;
    color: var(--yellow);
  }

  .back__name {
    position: absolute;
    left: 35px;
    font-weight: 600;
    font-size: 42px;
    color: var(--yellow);
    line-height: 1;
  }
  .back__role {
    position: absolute;
    left: 37px;
    font-weight: 500;
    font-size: 24px;
    color: var(--red);
    line-height: 1;
  }
  .card--top .back__name { top: 50px; }
  .card--top .back__role { top: 94px; }
  .card--bottom .back__name { top: 42px; }
  .card--bottom .back__role { top: 86px; }

  .contact {
    position: absolute;
    left: 37px;
    list-style: none;
    font-weight: 500;
    font-size: 16px;
    line-height: 28px;
    color: var(--yellow);
  }
  .card--top .contact { top: 200px; }
  .card--bottom .contact { top: 178px; }

  .emblem-area {
    position: absolute;
    right: 22px;
    width: 120px;
    height: 140px;
    border-radius: 50%;
    background: radial-gradient(ellipse at center, var(--emblem) 0, transparent 70%);
    opacity: 0.7;
  }
  .card--top .emblem-area { top: 170px; }
  .card--bottom .emblem-area { top: 150px; }
</style>
</head>
<body>
<main class="sheet">

  <section class="card card--top card--left card--front" aria-label="Front">
    <p class="wordmark">Lenny Marsh</p>
  </section>

  <section class="card card--top card--right card--back" aria-label="Back">
    <h1 class="back__name">Lenny Marsh</h1>
    <p class="back__role">DJ</p>
    <ul class="contact">
      <li>Cell : 310-555-0148</li>
      <li>Email : djlennymarsh@postvale.com</li>
      <li>Website : www.djlennymarsh.com</li>
    </ul>
    <div class="emblem-area" role="img" aria-label="Faint headphones emblem"></div>
  </section>

  <section class="card card--bottom card--left card--front" aria-label="Front">
    <p class="wordmark">Lenny Marsh</p>
  </section>

  <section class="card card--bottom card--right card--back" aria-label="Back">
    <h2 class="back__name">Lenny Marsh</h2>
    <p class="back__role">DJ</p>
    <ul class="contact">
      <li>Cell : 310-555-0148</li>
      <li>Email : bookings-kt@quillsoundagency.com</li>
      <li>Website : www.djlennymarsh.com</li>
      <li>twitter.com/djlennymarsh</li>
    </ul>
    <div class="emblem-area" role="img" aria-label="Faint headphones emblem"></div>
  </section>

</main>
</body>
</html>
```